Flyer Design for an electrical and security company trying to build local customers

I need a flyer design for a new company based in Sans Souci, Sydney 2219 called "Harbor Quill Dune Electrical and Security" also "HQD Electrical and Security". We are electrical contractors who are looking for more local work including emergency service calls and any project work including renovations or new constructions in the local area. I would like everyone in the area to know I am new and that I am available 24 hours a day 7 days a week. I would like to see designs that use the logo colours. Would also like the font of the entire design to be "juice bold".

Electrical

• juice bold

Requirements
Must have
• Must use the colours of the original logo and also have the information from the rear of the card. Must also have services buttons like the website picture attached.

```html
<!DOCTYPE html>
<html lang="en">
<head>
<meta charset="utf-8">
<title>Harbor Quill Dune Electrical and Security – Flyer</title>
<link rel="stylesheet" href="https://fonts.googleapis.com/css2?family=Baumans&family=Comfortaa:wght@500;700&display=swap">
<style>
  :root {
    --blue: #2eaee3;
    --blue-dark: #1e8fc2;
    --orange: #ef7d3a;
    --peach: #f4b48c;
    --ink: #2f2f2f;
    --grey: #7b7b7b;
    --paper: #ffffff;
    --backdrop: #e4e4e4;
  }
  * { box-sizing: border-box; margin: 0; padding: 0; }
  html, body { width: 1200px; height: 800px; overflow: hidden; }
  body {
    background: var(--backdrop);
    font-family: "Comfortaa", sans-serif;
    color: var(--ink);
    position: relative;
  }
  .spread {
    position: absolute; left: 40px; top: 40px;
    width: 1120px; height: 720px;
    display: flex;
    box-shadow: 0 8px 24px rgba(0,0,0,.18);
  }
  .page {
    position: relative; width: 560px; height: 720px;
    background: var(--paper); overflow: hidden;
  }
  .page--left { border-right: 1px solid #e6e6e6; }
  .band-svg { position: absolute; left: 0; width: 560px; display: block; }

  /* Left page header */
  .contact {
    position: absolute; left: 26px; top: 22px;
    color: #fff; font-family: "Baumans", sans-serif;
    font-size: 15px; line-height: 1.45; letter-spacing: .5px;
  }

  /* Services */
  .services {
    position: absolute; left: 20px; top: 140px; width: 520px;
    display: grid; grid-template-columns: repeat(4, 1fr);
    row-gap: 22px; column-gap: 6px;
  }
  .svc { text-align: center; }
  .svc-icon {
    width: 38px; height: 38px; margin: 0 auto 5px;
    border-radius: 50%; border: 2px solid #4a6f86;
    display: flex; align-items: center; justify-content: center;
  }
  .svc-icon svg { width: 20px; height: 20px; stroke: var(--ink); fill: none; stroke-width: 1.8; stroke-linecap: round; stroke-linejoin: round; }
  .svc-icon--hot { background: var(--orange); border-color: var(--orange); }
  .svc-icon--hot svg { stroke: #fff; }
  .svc-title { font-family: "Baumans", sans-serif; font-size: 10.5px; margin-bottom: 4px; }
  .svc-text { font-size: 7.5px; line-height: 1.25; color: var(--ink); font-weight: 700; }
  .services .svc--offset { grid-column: 1; }

  /* Photo strip */
  .photo-strip {
    position: absolute; left: 22px; top: 574px; width: 516px;
    display: flex; gap: 10px;
  }
  .photo {
    flex: 1; height: 96px;
    border: 3px solid #fff; box-shadow: 0 1px 4px rgba(0,0,0,.25);
  }
  .photo--a { background: linear-gradient(135deg, #9fb1bd, #5d6a72); }
  .photo--b { background: linear-gradient(135deg, #c8b79a, #6f6a60); }
  .photo--c { background: linear-gradient(135deg, #d5c2a0, #7a8a96); }
  .photo--d { background: linear-gradient(135deg, #c7b08e, #6e5e4c); }
  .photo--e { background: linear-gradient(135deg, #b9c7cf, #7f8a7c); }

  .footer-band { position: absolute; left: 0; bottom: 0; width: 100%; height: 22px; background: var(--blue); }
  .footer-band::before { content: ""; position: absolute; left: 0; right: 0; top: -5px; height: 3px; background: var(--peach); }

  /* Right page */
  .brand {
    position: absolute; left: 24px; top: 24px; display: flex; align-items: center; gap: 7px;
  }
  .brand-dot { width: 12px; height: 12px; border-radius: 50%; background: var(--orange); }
  .brand-name { font-family: "Baumans", sans-serif; font-size: 16px; color: var(--blue-dark); line-height: 1.05; }
  .brand-name small { display: block; font-size: 9px; }

  .hero { position: absolute; top: 0; left: 0; width: 560px; height: 250px; }

  .tagline {
    position: absolute; right: 28px; top: 248px; width: 330px;
    text-align: right; font-family: "Baumans", sans-serif;
    font-size: 13px; line-height: 1.3; color: var(--ink);
  }
  .about-title {
    position: absolute; left: 30px; top: 338px;
    font-family: "Baumans", sans-serif; font-size: 19px; color: var(--grey);
    padding-bottom: 4px; border-bottom: 2px solid var(--peach);
  }
  .about-title .about-name { color: var(--blue); }
  .about-text {
    position: absolute; left: 30px; top: 378px; width: 500px;
    font-size: 10.5px; line-height: 1.5; font-weight: 700;
  }
  .sectors-title {
    position: absolute; left: 30px; top: 498px;
    font-family: "Baumans", sans-serif; font-size: 19px; color: var(--ink);
    padding-bottom: 4px; border-bottom: 2px solid var(--peach);
  }
  .sectors {
    position: absolute; left: 40px; top: 548px; display: flex; gap: 56px;
  }
  .sector { text-align: center; width: 70px; }
  .sector-icon {
    width: 44px; height: 44px; margin: 0 auto 8px; border-radius: 50%;
    background: var(--orange); display: flex; align-items: center; justify-content: center;
  }
  .sector-icon svg { width: 24px; height: 24px; fill: none; stroke: #fff; stroke-width: 2; stroke-linejoin: round; }
  .sector-label { font-family: "Baumans", sans-serif; font-size: 10px; }
</style>
</head>
<body>
<main class="spread">

  <!-- Left page: services -->
  <section class="page page--left">
    <svg class="band-svg" style="top:0" width="560" height="140" viewBox="0 0 560 140" aria-hidden="true">
      <path d="M0 0 H560 V80 C430 58 320 120 190 112 C110 107 50 96 0 100 Z" fill="var(--blue)"/>
      <path d="M0 108 C60 104 120 114 190 118 C320 126 430 66 560 88" fill="none" stroke="var(--peach)" stroke-width="4"/>
    </svg>
    <div class="contact">
      <p>Call Us Today 1300 555 014</p>
      <p>Visit Us www.HarborQuillDune.com</p>
    </div>

    <div class="services">
      <div class="svc">
        <div class="svc-icon svc-icon--hot"><svg viewBox="0 0 24 24"><circle cx="12" cy="12" r="9"/><path d="M12 7v5l3 2"/></svg></div>
        <p class="svc-title">24 Hour Emergency Services</p>
        <p class="svc-text">Lorem ipsum dolor sit consectetuer adipiscing diam nonummy</p>
      </div>
      <div class="svc">
        <div class="svc-icon"><svg viewBox="0 0 24 24"><path d="M5 19l9-9M14 4a4 4 0 0 0 5 5l-2 2-5-5zM5 5l14 14"/></svg></div>
        <p class="svc-title">New Installations</p>
        <p class="svc-text">Lorem ipsum dolor sit consectetuer adipiscing diam nonummy</p>
      </div>
      <div class="svc">
        <div class="svc-icon"><svg viewBox="0 0 24 24"><path d="M3 12l9-7 9 7M6 10v9h12v-9"/></svg></div>
        <p class="svc-title">Repairs</p>
        <p class="svc-text">Lorem ipsum dolor sit consectetuer adipiscing diam nonummy</p>
      </div>
      <div class="svc">
        <div class="svc-icon"><svg viewBox="0 0 24 24"><path d="M3 12l9-7 9 7M6 10v9h12v-9M10 19v-5h4v5"/></svg></div>
        <p class="svc-title">Maintenance</p>
        <p class="svc-text">Lorem ipsum dolor sit consectetuer adipiscing diam nonummy</p>
      </div>

      <div class="svc">
        <div class="svc-icon"><svg viewBox="0 0 24 24"><path d="M3 12l9-7 9 7M6 10v9h12v-9M10 13h4v3h-4z"/></svg></div>
        <p class="svc-title">Renovations/Extensions</p>
        <p class="svc-text">Lorem ipsum dolor sit consectetuer adipiscing diam nonummy</p>
      </div>
      <div class="svc">
        <div class="svc-icon"><svg viewBox="0 0 24 24"><path d="M4 20c4-2 4-8 8-8s4-6 8-8M15 4l5 0 0 5"/></svg></div>
        <p class="svc-title">Re-Wiring</p>
        <p class="svc-text">Lorem ipsum dolor sit consectetuer adipiscing diam nonummy</p>
      </div>
      <div class="svc">
        <div class="svc-icon"><svg viewBox="0 0 24 24"><rect x="3" y="5" width="18" height="11" rx="1"/><path d="M8 20h8M12 16v4"/></svg></div>
        <p class="svc-title">Home Theatre</p>
        <p class="svc-text">Lorem ipsum dolor sit consectetuer adipiscing diam nonummy</p>
      </div>
      <div class="svc">
        <div class="svc-icon"><svg viewBox="0 0 24 24"><rect x="6" y="3" width="12" height="18" rx="2"/><circle cx="12" cy="14" r="3"/><circle cx="12" cy="7" r="1"/></svg></div>
        <p class="svc-title">Surround Sound</p>
        <p class="svc-text">Lorem ipsum dolor sit consectetuer adipiscing diam nonummy</p>
      </div>

      <div class="svc">
        <div class="svc-icon"><svg viewBox="0 0 24 24"><rect x="3" y="5" width="18" height="12" rx="2"/><path d="M9 21h6"/></svg></div>
        <p class="svc-title">Wall TV's</p>
        <p class="svc-text">Lorem ipsum dolor sit consectetuer adipiscing diam nonummy</p>
      </div>
      <div class="svc">
        <div class="svc-icon"><svg viewBox="0 0 24 24"><path d="M4 9h10a3 3 0 0 1 3 3v2M8 9V6h4v3M17 17v2"/></svg></div>
        <p class="svc-title">Electric Hot Water</p>
        <p class="svc-text">Lorem ipsum dolor sit consectetuer adipiscing diam nonummy</p>
      </div>
      <div class="svc">
        <div class="svc-icon"><svg viewBox="0 0 24 24"><rect x="5" y="4" width="14" height="16" rx="1"/><path d="M5 9h14"/><circle cx="12" cy="14" r="2.5"/></svg></div>
        <p class="svc-title">Stoves</p>
        <p class="svc-text">Lorem ipsum dolor sit consectetuer adipiscing diam nonummy</p>
      </div>
      <div class="svc">
        <div class="svc-icon"><svg viewBox="0 0 24 24"><rect x="4" y="5" width="16" height="14" rx="2"/></svg></div>
        <p class="svc-title">Cooktops</p>
        <p class="svc-text">Lorem ipsum dolor sit consectetuer adipiscing diam nonummy</p>
      </div>

      <div class="svc">
        <div class="svc-icon"><svg viewBox="0 0 24 24"><path d="M12 3v6M5 12h14M7 12l-3 6M17 12l3 6M12 12v4"/></svg></div>
        <p class="svc-title">Lighting &amp; Ceiling Fans</p>
        <p class="svc-text">Lorem ipsum dolor sit consectetuer adipiscing diam nonummy</p>
      </div>
      <div class="svc">
        <div class="svc-icon"><svg viewBox="0 0 24 24"><path d="M5 8c0-2 14-2 14 0v2h-4V8H9v2H5zM7 11l-2 8h14l-2-8"/><circle cx="12" cy="15" r="2"/></svg></div>
        <p class="svc-title">Telephone</p>
        <p class="svc-text">Lorem ipsum dolor sit consectetuer adipiscing diam nonummy</p>
      </div>
      <div class="svc">
        <div class="svc-icon"><svg viewBox="0 0 24 24"><path d="M3 9l12-3 2 5-12 3zM7 13l1 5h3"/></svg></div>
        <p class="svc-title">Security System</p>
        <p class="svc-text">Lorem ipsum dolor sit consectetuer adipiscing diam nonummy</p>
      </div>
    </div>

    <div class="photo-strip">
      <div class="photo photo--a" role="img" aria-label="Electrician working on a ceiling fitting"></div>
      <div class="photo photo--b" role="img" aria-label="Interior fit-out work site"></div>
      <div class="photo photo--c" role="img" aria-label="Construction framing with wiring"></div>
      <div class="photo photo--d" role="img" aria-label="Commercial renovation in progress"></div>
      <div class="photo photo--e" role="img" aria-label="Building site with scissor lift"></div>
    </div>
    <div class="footer-band"></div>
  </section>

  <!-- Right page: about -->
  <section class="page page--right">
    <svg class="hero" width="560" height="250" viewBox="0 0 560 250" role="img" aria-label="Photo of a modern open-plan home interior with a smiling client giving thumbs up">
      <defs>
        <linearGradient id="heroTone" x1="0" y1="0" x2="1" y2="1">
          <stop offset="0" stop-color="#e9e6e1"/>
          <stop offset=".55" stop-color="#9d8a74"/>
          <stop offset="1" stop-color="#5b4a3a"/>
        </linearGradient>
      </defs>
      <path d="M120 0 H560 V150 C470 188 380 200 280 205 C200 209 150 200 120 185 Z" fill="url(#heroTone)"/>
      <path d="M80 200 C180 226 320 222 430 190 C490 172 530 160 560 158 V175 C520 180 470 200 420 214 C300 245 170 240 80 210 Z" fill="var(--blue)"/>
      <path d="M78 214 C180 246 320 244 430 214 C490 198 530 186 560 184" fill="none" stroke="var(--peach)" stroke-width="4"/>
    </svg>

    <div class="brand">
      <span class="brand-dot"></span>
      <p class="brand-name">Harbor Quill Dune<small>electrical and security</small></p>
    </div>

    <p class="tagline">We Do All House Renovations, Construction, Commercial, 24 Hour Emergency Services, New Installations, Repairs, Maintenance, Home Theater And So On...</p>

    <h2 class="about-title">About <span class="about-name">Harbor Quill Dune</span></h2>
    <p class="about-text">Lorem ipsum dolor sit amet, consectetuer adipiscing elit, sed diam nonummy nibh euismod tincidunt ut laoreet dolore magna aliquam erat volutpat. Ut wisi enim ad minim veniam, quis nostrud exerci tation ullamcorper suscipit lobortis nisl ut aliquip modo consequat. Duis autem vel eum iriure dolor in hendrerit in vul putate velit esse mtie consequat, vel illum dolore eu feugiat nulla facilisis at vero eros et accumsan et iusto odio dignissim qui blandit praesent luptatum zzril delenit augue duis dolore te feugait nulla facilisi.</p>

    <h2 class="sectors-title">Sectors We Serve</h2>
    <div class="sectors">
      <div class="sector">
        <div class="sector-icon"><svg viewBox="0 0 24 24"><path d="M3 12l9-8 9 8M6 10v10h12V10M10 20v-6h4v6"/></svg></div>
        <p class="sector-label">Residential</p>
      </div>
      <div class="sector">
        <div class="sector-icon"><svg viewBox="0 0 24 24"><path d="M4 20V8h7v12M11 20V4h9v16M3 20h18M14 8h3M14 12h3M14 16h3"/></svg></div>
        <p class="sector-label">Commercial</p>
      </div>
      <div class="sector">
        <div class="sector-icon"><svg viewBox="0 0 24 24"><path d="M3 20V10l5 3v-3l5 3v-3l5 3V4h3v16z"/></svg></div>
        <p class="sector-label">Industrial</p>
      </div>
    </div>
    <div class="footer-band"></div>
  </section>

</main>
</body>
</html>
```